Business card for utility of the future

I need a business card template designed for brookvane. We provide sustainable water, energy and waste services to homes.

The card should include name, position, email address, phone number, website and our logo (attached). I would like it to convey professionalism and creativity.

Target Market(s)

Homeowners, investors, corporate partners.

Industry/Entity Type

Utility

Contact Information for Business Card

The card should include name, position, email address, phone number, website and our logo (attached).

```html
<!DOCTYPE html>
<html lang="en">
<head>
<meta charset="utf-8">
<title>brookvane — business card</title>
<link rel="stylesheet" href="https://fonts.googleapis.com/css2?family=Source+Sans+3:wght@400;600;700&display=swap">
<style>
  :root {
    --backdrop: #8f8f8f;
    --card-light: #e6e6e9;
    --card-accent: #c9735a;
    --brand-green: #5aa36b;
    --brand-orange: #d0714f;
    --ink: #45464a;
    --divider: #b9b9bd;
    --reverse-ink: #e7e3e1;
  }
  * { margin: 0; padding: 0; box-sizing: border-box; }
  html, body {
    width: 1105px;
    height: 1200px;
    overflow: hidden;
  }
  body {
    position: relative;
    background: var(--backdrop);
    font-family: "Source Sans 3", "Myriad Pro", sans-serif;
  }
  .card {
    position: absolute;
    left: 182px;
    width: 746px;
    height: 425px;
  }
  .card--front { top: 119px; background: var(--card-light); }
  .card--back  { top: 635px; background: var(--card-accent); }

  .wordmark {
    position: absolute;
    font-weight: 700;
    letter-spacing: -0.02em;
    line-height: 1;
    white-space: nowrap;
  }
  .card--front .wordmark {
    left: 93px;
    top: 118px;
    font-size: 68px;
    color: var(--brand-green);
  }
  .divider {
    position: absolute;
    left: 404px;
    top: 120px;
    width: 1px;
    height: 186px;
    background: var(--divider);
  }
  .contact {
    position: absolute;
    left: 439px;
    top: 124px;
  }
  .contact__name {
    font-size: 26px;
    font-weight: 600;
    color: var(--brand-green);
    line-height: 1.1;
  }
  .contact__role {
    font-size: 19px;
    color: var(--brand-orange);
    margin-top: 4px;
  }
  .contact__list {
    list-style: none;
    margin-top: 26px;
  }
  .contact__item {
    display: flex;
    align-items: center;
    gap: 13px;
    font-size: 19px;
    color: var(--ink);
    height: 29px;
  }
  .contact__icon {
    width: 18px;
    height: 18px;
    fill: var(--brand-green);
    flex: none;
  }

  .card--back .wordmark {
    left: 0;
    right: 0;
    top: 168px;
    text-align: center;
    font-size: 104px;
    color: var(--reverse-ink);
  }
  .site-url {
    position: absolute;
    left: 0;
    right: 0;
    top: 357px;
    text-align: center;
    font-size: 19px;
    letter-spacing: 0.52em;
    color: var(--reverse-ink);
  }
</style>
</head>
<body>
  <section class="card card--front" aria-label="Business card front">
    <div class="wordmark">brookvane</div>
    <div class="divider"></div>
    <div class="contact">
      <p class="contact__name">Daniel Reyes</p>
      <p class="contact__role">CEO/Founder</p>
      <ul class="contact__list">
        <li class="contact__item">
          <svg class="contact__icon" viewBox="0 0 24 24" aria-hidden="true"><path d="M6.6 10.8a15.1 15.1 0 0 0 6.6 6.6l2.2-2.2a1 1 0 0 1 1-.25 11.4 11.4 0 0 0 3.6.6 1 1 0 0 1 1 1V20a1 1 0 0 1-1 1A17 17 0 0 1 3 4a1 1 0 0 1 1-1h3.5a1 1 0 0 1 1 1c0 1.25.2 2.45.6 3.6a1 1 0 0 1-.25 1z"/></svg>
          555 014 2207
        </li>
        <li class="contact__item">
          <svg class="contact__icon" viewBox="0 0 24 24" aria-hidden="true"><path d="M3 5h18v14H3z M4.5 6.5 12 12l7.5-5.5" /><path d="M3 5h18L12 11.5z" fill="#fff" opacity=".35"/></svg>
          name@brookvane.com
        </li>
        <li class="contact__item">
          <svg class="contact__icon" viewBox="0 0 24 24" aria-hidden="true"><circle cx="12" cy="12" r="10"/><path d="M7 8c2 0 3 1 3 2.5S8 12 8 14s2 2 2 4M14 4.5c0 2 2 2 2 4s-2 2-1 4 3 1 4 3" stroke="#e6e6e9" stroke-width="1.6" fill="none"/></svg>
          www.brookvane.com
        </li>
      </ul>
    </div>
  </section>

  <section class="card card--back" aria-label="Business card back">
    <div class="wordmark">brookvane</div>
    <p class="site-url">www.brookvane.com</p>
  </section>
</body>
</html>
```